Homecare Information Flyer

We require a brochure/ leaflet to be created which would provide healthcare information to our staff and patients on the topic of- Pressure Ulcers. The document would ideally be 3 fold. It should include our Logo/ Company Information (Marrowby Staffing).

I have attached-
- Logo
- Text/ Visual images to be included.

Industry/Entity Type

Healthcare

```html
<!DOCTYPE html>
<html lang="en">
<head>
<meta charset="utf-8">
<title>Marrowby Staffing – Pressure Area Care leaflet</title>
<link rel="stylesheet" href="https://fonts.googleapis.com/css2?family=Arimo:wght@400;700&family=Open+Sans:wght@300;400;700&display=swap">
<style>
  :root {
    --backdrop: #c7cbce;
    --forest: #2f6a2b;
    --lime: #cfe04c;
    --paper: #ffffff;
    --ink: #3a3a3a;
    --photo-blue: #9cc9e0;
    --map-tone: #e4e1da;
  }
  * { box-sizing: border-box; margin: 0; padding: 0; }
  html, body {
    width: 1200px; height: 800px; overflow: hidden;
    background: var(--backdrop);
    font-family: "Arimo", Arial, sans-serif;
    color: var(--ink);
  }
  .leaflet {
    position: absolute; left: 75px; top: 60px;
    width: 1050px; height: 680px;
    display: flex;
    box-shadow: 0 10px 30px rgba(0,0,0,.18);
  }
  .panel { position: relative; width: 350px; height: 100%; overflow: hidden; }

  /* Mission panel */
  .panel--mission { background: var(--paper); }
  .mission__band {
    position: absolute; left: 0; top: 36px; width: 100%; height: 58px;
    background: var(--lime);
  }
  .mission__title {
    position: absolute; left: 26px; top: 50px;
    font-size: 24px; font-weight: 700; color: var(--forest);
  }
  .mission__photo {
    position: absolute; left: 26px; top: 94px; width: 300px; height: 140px;
    background: linear-gradient(180deg, #e9eef1 0%, var(--photo-blue) 100%);
  }
  .mission__text {
    position: absolute; left: 26px; top: 252px; width: 300px;
    font-size: 10.6px; line-height: 1.32;
  }
  .mission__text p + p { margin-top: 11px; }

  /* Contact panel */
  .panel--contact { background: var(--forest); color: var(--paper); text-align: center; }
  .contact__map {
    position: absolute; left: 30px; top: 40px; width: 290px; height: 200px;
    background: var(--paper); padding: 8px;
  }
  .contact__map div { width: 100%; height: 100%; background: linear-gradient(160deg, var(--map-tone), #d6d3cb); }
  .contact__heading {
    position: absolute; left: 0; top: 290px; width: 100%;
    font-family: "Open Sans", Arial, sans-serif; font-weight: 300;
    font-size: 22px; line-height: 1.3;
  }
  .contact-block { font-size: 13px; line-height: 1.45; }
  .contact-block strong { font-weight: 700; }
  .contact-block .email { margin-top: 8px; font-size: 14px; }
  .contact-block .web { margin-top: 10px; font-size: 19px; font-weight: 700; }
  .panel--contact .contact-block { position: absolute; left: 0; top: 410px; width: 100%; }

  /* Cover panel */
  .panel--cover { background: var(--lime); text-align: center; }
  .cover__top {
    position: absolute; left: 0; top: 0; width: 100%; height: 178px;
    background: var(--paper);
  }
  .brand { position: absolute; left: 0; top: 40px; width: 100%; }
  .brand__dot {
    width: 62px; height: 62px; border-radius: 50%;
    background: var(--forest); margin: 0 auto 14px;
  }
  .brand__name { font-size: 26px; font-weight: 700; color: #4a4a4a; }
  .cover__stripes { position: absolute; left: 0; top: 178px; width: 100%; }
  .cover__title {
    position: absolute; left: 0; top: 236px; width: 100%;
    font-family: "Open Sans", Arial, sans-serif; font-weight: 400;
    font-size: 24px; line-height: 1.2; color: var(--forest);
  }
  .cover__subtitle {
    position: absolute; left: 0; top: 350px; width: 100%;
    font-size: 20px; font-weight: 700; color: #3d3d3d;
  }
  .panel--cover .contact-block { position: absolute; left: 0; top: 440px; width: 100%; color: #3d3d3d; }
</style>
</head>
<body>
<main class="leaflet">
  <section class="panel panel--mission">
    <div class="mission__band"></div>
    <h2 class="mission__title">Our mission</h2>
    <div class="mission__photo" role="img" aria-label="Photo of a smiling team of healthcare staff in scrubs"></div>
    <div class="mission__text">
      <p>Our mission is to ensure that our clients receive the highest level of service from Marrowby’s ambassadors while our staff are rewarded with the best rates of pay and benefits available. It is this trademark quality of our service that allows our organisation to develop, further improving our reputation and broadening the work opportunities for our staff.</p>
      <p>At Marrowby Staffing we understand that our busy Healthcare Professionals don’t want to spend endless hours completing paperwork so they can commence work with us. That’s why we have created a user-friendly, interactive website service where applications can be easily downloaded and completed, but also where our staff can be directly contacted by email, our accounts office can be contacted, timesheets can be printed and availability updated. We are driven to bringing our staff to the point at which they can be sent to work as quickly as possible. We will assist with your application as much as we can whether that involves helping with CVs, organising immunity profiles or your training needs, because we want you to be earning money for yourself as soon as possible with all your vetting requirements in place.</p>
      <p>Marrowby utilise the most modern allocation/finance package on the market to ensure our staff are offered the best work possible and that they are guaranteed to be paid each week with 100% accuracy.</p>
    </div>
  </section>

  <section class="panel panel--contact">
    <div class="contact__map"><div role="img" aria-label="Street map showing the office location"></div></div>
    <h2 class="contact__heading">We look forward<br>to hearing from you</h2>
    <address class="contact-block" style="font-style:normal">
      <p>Two Harrow Court<br>Kelbridge<br>London W9 4QT</p>
      <p><strong>Tel</strong> 0203 555 0142<br><strong>Fax</strong> 0203 555 0143</p>
      <p class="email"><strong>Email</strong> info@marrowbystaffing.co.uk</p>
      <p class="web">www.carewellguides.com</p>
    </address>
  </section>

  <section class="panel panel--cover">
    <div class="cover__top"></div>
    <div class="brand">
      <div class="brand__dot"></div>
      <p class="brand__name">Marrowby Staffing</p>
    </div>
    <svg class="cover__stripes" width="350" height="26" viewBox="0 0 350 26" aria-hidden="true">
      <rect x="0" y="0" width="350" height="5" fill="#2f6a2b"/>
      <rect x="0" y="10" width="350" height="5" fill="#2f6a2b"/>
      <rect x="0" y="20" width="350" height="5" fill="#2f6a2b"/>
    </svg>
    <h1 class="cover__title">Pressure<br>Area<br>Care</h1>
    <p class="cover__subtitle">A guide for patients</p>
    <address class="contact-block" style="font-style:normal">
      <p>Two Harrow Court<br>Kelbridge<br>London W9 4QT</p>
      <p><strong>Tel</strong> 0203 555 0142<br><strong>Fax</strong> 0203 555 0143</p>
      <p class="email"><strong>Email</strong> info@carewellguides.com</p>
      <p class="web">www.carewellguides.com</p>
    </address>
  </section>
</main>
</body>
</html>
```